bluefernworks.com website design

We're looking for a website design for Bluefernworks.com .
Bluefern is a manufacturer of high visibility traffic safety equipment and gear.. Our initial site will be a product catalog site featuring traffic cones . We will eventually expand to include traffic barriers, mesh signs, safety clothing and more. Our logo and product pictures can be found at bluefernworks.com .
Updates

Target Market(s)

We service a wide range of customers with our focus markets being construction, manufacturing and municipalities.

Industry/Entity Type

Safety Products

Number of Pages Required

1 page

Font styles to use
Sans Serif

Requirements
Must have
• company logo w/compatible color scheme

```html
<!DOCTYPE html>
<html lang="en">
<head>
<meta charset="utf-8">
<title>Bluefern Safety Products</title>
<link href="https://fonts.googleapis.com/css2?family=Montserrat:wght@400;500;600;700&display=swap" rel="stylesheet">
<style>
:root{
  --orange:#e8913f;
  --orange-dark:#e07f2a;
  --green:#6cb550;
  --dark:#333333;
  --panel:#505050;
  --text:#444444;
  --muted:#777777;
  --light:#f4f4f6;
  --line:#e2e2e2;
  --navy:#4a5590;
  --red:#e53935;
}
*{box-sizing:border-box;margin:0;padding:0}
html,body{width:1200px;height:3130px;overflow:hidden}
body{font-family:'Montserrat',sans-serif;color:var(--text);background:#fff;font-size:11px}
.wrap{position:relative;width:882px;margin-left:159px;height:100%}
section,header,footer{position:relative;width:1200px;overflow:hidden}
.abs{position:absolute}

/* top bar */
.topbar{height:24px;background:var(--dark);color:#fff;font-size:10px}
.social-mini{position:absolute;left:0;top:6px;display:flex;gap:3px}
.social-mini span{width:11px;height:11px;border:1px solid #aaa}
.hours{position:absolute;right:0;top:6px}

/* header */
.header{height:61px;background:#fff}
.brand{position:absolute;left:0;top:10px;display:flex;align-items:center;gap:6px}
.brand-dot{width:14px;height:14px;border-radius:50%;background:var(--orange)}
.brand-name{font-weight:700;font-size:20px;color:var(--orange)}
.search{position:absolute;left:225px;top:13px;width:432px;height:31px;display:flex;border:1px solid #ccc}
.search input{flex:1;border:0;padding:0 12px;font:400 9px 'Montserrat',sans-serif;color:#555}
.search button{width:92px;border:0;background:var(--green);color:#fff;font:500 10px 'Montserrat',sans-serif}
.icons{position:absolute;right:0;top:22px;display:flex;gap:10px;align-items:center}

/* nav */
.nav{height:34px;background:var(--green);color:#fff}
.cat{position:absolute;left:0;top:0;width:149px;height:34px;background:#4b4b4b;display:flex;align-items:center;padding-left:16px;gap:10px;font-size:10px}
.menu{position:absolute;left:318px;top:11px;display:flex;gap:22px;font-size:10px}
.order{position:absolute;right:0;top:5px;font-size:8px;display:flex;gap:8px;align-items:center}
.order strong{display:block;font-size:10px;font-weight:500}

/* hero */
.hero{height:331px;background:var(--light)}
.hero h1{position:absolute;left:297px;top:98px;font-size:46px;font-weight:700;color:#444;letter-spacing:1px}
.hero h1 em{font-style:normal;font-weight:400;color:var(--orange)}
.hero p{position:absolute;left:400px;top:166px;width:420px;text-align:center;font-size:11px;line-height:14px;color:#666}
.btn-dark{background:#000;color:#fff;font-size:8px;font-weight:600;display:inline-flex;align-items:center;justify-content:center}
.hero .btn-dark{position:absolute;left:556px;top:214px;width:87px;height:27px}
.hero-img{position:absolute;left:868px;top:34px;width:260px;height:262px;border-radius:40% 40% 30% 30%;background:radial-gradient(circle at 40% 45%,#e2c98a,#b8b8b8 60%,transparent 72%)}
.dots{position:absolute;left:574px;top:280px;display:flex;gap:4px;align-items:center}
.dots i{width:5px;height:5px;border-radius:3px;background:#ddd}
.dots i.on{width:16px;background:var(--orange)}

/* features */
.features{height:194px}
.feature{position:absolute;top:49px;width:207px;height:96px;border:1px solid var(--line);text-align:center;padding-top:14px}
.feature h3{font-size:11px;font-weight:600;color:var(--orange);margin-top:6px}
.feature a{display:inline-block;margin-top:8px;font-size:8px;font-weight:600;color:#333;text-decoration:underline}

/* promo */
.promo{height:263px;background:var(--light)}
.promo-a{position:absolute;left:0;top:53px;width:250px;height:158px;background:var(--orange);color:#fff;text-align:center;padding-top:40px;font-size:15px;letter-spacing:2px;line-height:23px}
.promo-a span{color:#f7c9a0}
.btn-grey{display:inline-flex;align-items:center;justify-content:center;background:#4b4b4b;color:#fff;font-size:9px;letter-spacing:0}
.promo-a .btn-grey{margin-top:20px;width:83px;height:24px}
.promo-b{position:absolute;left:289px;top:53px;width:303px;height:158px;border:2px solid #222;background:#fff;text-align:center;padding-top:34px;font-size:11px;color:#444}
.code{display:inline-block;margin:10px 0;border:1px solid #ccc;padding:4px 12px;font-size:24px;color:var(--orange);letter-spacing:1px}
.promo-b p.b{font-weight:500;font-size:11px;color:#222}
.promo-c{position:absolute;left:632px;top:53px;width:250px;height:158px;background:var(--orange);color:#fff}
.promo-c .t{position:absolute;left:9px;top:11px;font-size:11px;line-height:13px}
.promo-c .btn-grey{position:absolute;left:9px;top:120px;width:84px;height:24px}
.promo-c .img{position:absolute;left:10px;top:10px;width:190px;height:100px;background:linear-gradient(90deg,#d8d8d8,#b0b0b0);opacity:.55;border-radius:6px}
.promo-c .side{position:absolute;right:4px;bottom:8px;writing-mode:vertical-rl;transform:rotate(180deg);font-size:15px;letter-spacing:1px}

/* product block */
.products{height:394px}
.side-panel{position:absolute;left:0;top:45px;width:207px;height:298px;background:var(--panel);color:#fff;text-align:center;padding-top:44px}
.side-panel h2{font-size:15px;font-weight:400;letter-spacing:1px}
.side-panel p{font-size:9px;line-height:12px;margin:7px 14px 0}
.btn-white{display:inline-block;margin-top:18px;width:87px;height:26px;line-height:26px;background:#fff;color:var(--navy);font-size:9px}
.gloves{width:66px;height:96px;margin:18px auto 0;background:linear-gradient(180deg,#8fcdf0,#4ea7de);border-radius:20px 20px 8px 8px}
.block-head{position:absolute;left:225px;top:41px;width:657px;height:22px;border-bottom:1px solid var(--line);font-size:12px;font-weight:600;color:#333}
.block-head span{display:inline-block;height:22px;border-bottom:2px solid var(--orange)}
.block-head a{position:absolute;right:0;top:4px;font-size:8px;font-weight:600;text-decoration:underline;color:#333}
.cards{position:absolute;left:225px;top:74px;width:657px;height:270px;display:flex}
.card{position:relative;width:225px;height:100%;border-right:1px solid #eee;padding:0 9px}
.badge{position:absolute;right:8px;top:12px;height:12px;padding:0 5px;border-radius:6px;background:var(--red);color:#fff;font-size:7px;line-height:12px}
.badge.new{background:#5bd07e}
.prod-img{margin:8px auto 0;width:120px;height:136px;background:radial-gradient(ellipse at center,#f08c3c 30%,#e9e9e9 75%,#fff)}
.card h4{font-size:10px;font-weight:500;color:var(--orange);margin-top:0}
.stars{color:#f4b400;font-size:11px;letter-spacing:2px;margin-top:2px}
.card p{font-size:8.5px;line-height:10px;color:#666;margin-top:5px}
.price{position:absolute;left:9px;bottom:12px;font-size:11px;color:var(--green)}
.price s{color:#aaa;margin-right:8px}
.btn-cart{position:absolute;right:9px;bottom:8px;width:78px;height:23px;background:#222;color:#fff;font-size:7px;display:flex;align-items:center;justify-content:center;gap:4px}
.arrow{position:absolute;width:24px;height:24px;background:#333;color:#fff;display:flex;align-items:center;justify-content:center}

/* special */
.special{height:482px;background:var(--light)}
.special-left{position:absolute;left:0;top:0;width:606px;height:482px;background:linear-gradient(120deg,#5a6398,#3f4a85);color:#fff}
.special-left h2{position:absolute;left:89px;top:122px;font-size:19px;font-weight:500;letter-spacing:.5px}
.special-left .lead{position:absolute;left:89px;top:165px;width:440px;font-size:13px;line-height:16px}
.special-left .body{position:absolute;left:89px;top:210px;width:475px;font-size:10.5px;line-height:14px}
.count{position:absolute;left:189px;top:304px;display:flex;gap:8px}
.count div{width:52px;text-align:center;font-size:11px}
.count b{display:block;height:52px;line-height:52px;background:var(--orange);font-size:25px;font-weight:600;margin-bottom:4px}
.offer-card{position:absolute;left:653px;top:124px;width:363px;height:203px;border:2px solid var(--red);background:#fff}
.offer-card .prod-img{position:absolute;left:22px;top:36px;margin:0;width:120px;height:120px}
.offer-card .info{position:absolute;left:158px;top:38px;width:190px}

/* black */
.best{height:428px;background:#000;color:#fff}
.best .k{position:absolute;left:136px;top:47px;font-size:11px;font-weight:500}
.best h2{position:absolute;left:136px;top:63px;font-size:21px;font-weight:600}
.best .btn{position:absolute;left:958px;top:59px;width:83px;height:24px;background:var(--orange);font-size:9px;display:flex;align-items:center;justify-content:center}
.best-card{position:absolute;top:109px;width:432px;height:258px;background:#f6f6f6;color:#333;overflow:hidden}
.best-card h3{position:absolute;left:22px;top:75px;font-size:15px;font-weight:600;letter-spacing:2px;color:var(--orange)}
.best-card p{position:absolute;left:22px;top:103px;width:200px;font-size:9px;line-height:15px;color:#555}
.best-card .go{position:absolute;left:22px;top:163px;width:83px;height:23px;background:var(--green);color:#fff;font-size:9px;display:flex;align-items:center;justify-content:center}
.best-card .prod-img{position:absolute;right:40px;top:35px;margin:0;width:150px;height:200px}
.corner{position:absolute;right:0;top:0;width:0;height:0;border-top:56px solid var(--red);border-left:56px solid transparent}
.corner-t{position:absolute;right:4px;top:14px;transform:rotate(45deg);color:#fff;font-size:10px}

/* newsletter */
.news{height:237px;background:var(--orange);color:#fff;text-align:center}
.news h2{position:absolute;left:0;width:1200px;top:72px;font-size:19px;font-weight:400;letter-spacing:1px}
.news p{position:absolute;left:0;width:1200px;top:103px;font-size:13px}
.news form{position:absolute;left:384px;top:136px;width:431px;height:36px;display:flex}
.news input{flex:1;border:0;padding:0 18px;font:italic 400 11px 'Montserrat',sans-serif;color:#555}
.news button{width:113px;border:0;background:#111;color:#fff;font:500 9px 'Montserrat',sans-serif}

/* footer */
.footer{height:252px;background:#f7f7f7}
.footer .brand{top:40px}
.footer .about{position:absolute;left:0;top:98px;width:270px;font-size:10px;line-height:15px;color:#bbb}
.footer .soc{position:absolute;left:0;top:176px;display:flex;gap:6px}
.footer .soc span{width:21px;height:21px;background:var(--orange)}
.fcol{position:absolute;top:45px;font-size:10px;line-height:19px;color:#666}
.fcol h4{font-size:10px;font-weight:600;color:var(--orange);margin-bottom:6px}
.cards-pay{display:flex;gap:6px;margin-top:10px}
.cards-pay span{width:36px;height:22px;background:#fff;border:1px solid #ddd}
.copy{height:36px;background:#3b3b3b;color:#fff;font-size:9px;text-align:center;line-height:36px}
</style>
</head>
<body>

<header class="topbar">
  <div class="wrap">
    <div class="social-mini"><span></span><span></span><span></span><span></span></div>
    <div class="hours">Mon to Fri 9:30AM - 5:00PM</div>
  </div>
</header>

<header class="header">
  <div class="wrap">
    <div class="brand"><span class="brand-dot"></span><span class="brand-name">Bluefern</span></div>
    <div class="search"><input value="Search Entire Store here"><button>SEARCH</button></div>
    <div class="icons">
      <svg width="18" height="16" viewBox="0 0 18 16"><path d="M9 15 2 8a4 4 0 0 1 7-5 4 4 0 0 1 7 5z" fill="none" stroke="#333" stroke-width="1.4"/></svg>
      <svg width="17" height="17" viewBox="0 0 17 17"><circle cx="8.5" cy="8.5" r="7.5" fill="none" stroke="#333" stroke-width="1.3"/><circle cx="8.5" cy="7" r="2.6" fill="none" stroke="#333" stroke-width="1.3"/><path d="M3.5 14a6 6 0 0 1 10 0" fill="none" stroke="#333" stroke-width="1.3"/></svg>
      <svg width="26" height="17" viewBox="0 0 26 17"><rect x="1" y="5" width="14" height="11" fill="none" stroke="#333" stroke-width="1.4"/><path d="M4.5 5V3a3.5 3.5 0 0 1 7 0v2" fill="none" stroke="#333" stroke-width="1.4"/><text x="17" y="15" font-size="7" fill="#333" font-family="Montserrat,sans-serif">05</text></svg>
    </div>
  </div>
</header>

<nav class="nav">
  <div class="wrap">
    <div class="cat">
      <svg width="14" height="11"><rect y="0" width="14" height="2" fill="#fff"/><rect y="4.5" width="14" height="2" fill="#fff"/><rect y="9" width="14" height="2" fill="#fff"/></svg>
      <span>All Categories</span>
      <svg width="10" height="6" style="margin-left:22px"><path d="M1 1l4 4 4-4" stroke="#fff" fill="none"/></svg>
    </div>
    <div class="menu"><span>Home</span><span>About</span><span>Shop ⌄</span><span>News</span><span>Contact</span></div>
    <div class="order">
      <svg width="22" height="22" viewBox="0 0 22 22"><path d="M5 2l4 4-2 3a11 11 0 0 0 6 6l3-2 4 4-3 3C9 20 2 13 2 5z" fill="none" stroke="#fff" stroke-width="1.3"/></svg>
      <div>Order Now<strong>1234567890</strong></div>
    </div>
  </div>
</nav>

<section class="hero">
  <svg class="abs" style="left:46px;top:151px" width="18" height="32"><path d="M16 2 2 16l14 14" stroke="#222" stroke-width="1.6" fill="none"/></svg>
  <svg class="abs" style="left:1136px;top:151px" width="18" height="32"><path d="M2 2l14 14L2 30" stroke="#222" stroke-width="1.6" fill="none"/></svg>
  <div class="hero-img" role="img" aria-label="Brass padlock with a ring of keys"></div>
  <h1>BULK ORDER <em>DISCOUNT</em></h1>
  <p>Lorem ipsum dolor sit amet, consectetur adipiscing elit. Etiam sollicitudin metus eros, elementum pulvinar ante rutrum vel.</p>
  <a class="btn-dark">SHOP NOW</a>
  <div class="dots"><i></i><i class="on"></i><i></i></div>
</section>

<section class="features">
  <div class="wrap">
    <div class="feature" style="left:0">
      <svg width="34" height="26" viewBox="0 0 34 26"><path d="M8 4h15v14H8zM23 9h6l4 5v4h-10" fill="none" stroke="#2a2f7a" stroke-width="1.6"/><circle cx="12" cy="20" r="3" fill="#fff" stroke="#2a2f7a" stroke-width="1.6"/><circle cx="27" cy="20" r="3" fill="#fff" stroke="#2a2f7a" stroke-width="1.6"/><path d="M1 8h5M2 12h5" stroke="#e8913f" stroke-width="1.6"/></svg>
      <h3>FAST DELIVERY</h3><a>MORE DETAILS</a>
    </div>
    <div class="feature" style="left:225px">
      <svg width="30" height="26" viewBox="0 0 30 26"><rect x="5" y="2" width="20" height="22" fill="none" stroke="#2a2f7a" stroke-width="1.6"/><path d="M10 12h10l-3-3M20 16H10l3 3" fill="none" stroke="#e8913f" stroke-width="1.6"/></svg>
      <h3>EASY RETURN</h3><a>VIEW MORE</a>
    </div>
    <div class="feature" style="left:449px">
      <svg width="30" height="26" viewBox="0 0 30 26"><circle cx="15" cy="13" r="10" fill="none" stroke="#2a2f7a" stroke-width="1.6"/><text x="8.5" y="17" font-size="9" font-weight="700" fill="#e8913f" font-family="Montserrat,sans-serif">24</text></svg>
      <h3>24/7 CUSTOMER SUPPORT</h3><a>LEARN MORE</a>
    </div>
    <div class="feature" style="left:674px">
      <svg width="32" height="26" viewBox="0 0 32 26"><rect x="3" y="6" width="22" height="16" fill="none" stroke="#2a2f7a" stroke-width="1.6"/><path d="M3 11h22" stroke="#2a2f7a" stroke-width="1.6"/><path d="M21 5l3 3 6-6" stroke="#e8913f" stroke-width="1.6" fill="none"/></svg>
      <h3>100% PAYMENT SECURE</h3><a>MORE INFO</a>
    </div>
  </div>
</section>

<section class="promo">
  <div class="wrap">
    <div class="promo-a">UP TO <span>60% OFF!</span><br>ALL BRANDS<br><a class="btn-grey">SHOP NOW</a></div>
    <div class="promo-b">Use Promo Code<br><span class="code">50FOR50</span><p class="b">Get Extra 30% off on 1st Order</p></div>
    <div class="promo-c">
      <div class="img" role="img" aria-label="Door lock cylinder, mortise lock and cabinet lock"></div>
      <div class="t">SALE UP TO<br>35% OFF</div>
      <a class="btn-grey">SHOP NOW</a>
      <div class="side">BEST OFFER</div>
    </div>
  </div>
</section>

<section class="products">
  <div class="wrap">
    <div class="side-panel">
      <h2>BEST SELLERS</h2>
      <p>Lorem ipsum dolor sit amet, consectetur adipiscing elit. Explicabo quam</p>
      <a class="btn-white">Shop Now!</a>
      <div class="gloves" role="img" aria-label="Pair of blue nitrile gloves"></div>
    </div>
    <div class="block-head"><span>Best Sellers</span><a>SHOP ALL</a></div>
    <div class="cards">
      <div class="card"><span class="badge">-10%</span><div class="prod-img" role="img" aria-label="Orange hi-vis work shirt"></div><h4>RIM CYLINDERS</h4><div class="stars">★★★★★</div><p>Aliquam bibendum lacus a turpis eleifend, et molestie turpis gravida. Cras sit amet augue quis orci rtrum pretium vel id quam.....</p><div class="price"><s>$55.00</s>$35.00</div><a class="btn-cart">ADD TO CART ▢</a></div>
      <div class="card"><span class="badge new">NEW</span><div class="prod-img" role="img" aria-label="Orange safety helmet with visor and ear muffs"></div><h4>RIM CYLINDERS</h4><div class="stars">★★★★★</div><p>Aliquam bibendum lacus a turpis eleifend, et molestie turpis gravida. Cras sit amet augue quis orci rtrum pretium vel id quam.....</p><div class="price"><s>$55.00</s>$35.00</div><a class="btn-cart">ADD TO CART ▢</a></div>
      <div class="card" style="border:0"><span class="badge">-10%</span><div class="prod-img" role="img" aria-label="Orange chainsaw bar case"></div><h4>RIM CYLINDERS</h4><div class="stars">★★★★★</div><p>Aliquam bibendum lacus a turpis eleifend, et molestie turpis gravida. Cras sit amet augue quis orci rtrum pretium vel id quam.....</p><div class="price"><s>$55.00</s>$35.00</div><a class="btn-cart">ADD TO CART ▢</a></div>
    </div>
    <div class="arrow" style="left:225px;top:165px">‹</div>
    <div class="arrow" style="left:858px;top:165px">›</div>
  </div>
</section>

<section class="special">
  <div class="special-left" role="img" aria-label="Support agent wearing a headset, tinted blue">
    <h2>SPECIAL OFFER OF THE WEEK</h2>
    <p class="lead">Lorem ipsum dolor sit amet, consectetur adipiscing elit. Etiam sollicitudin metus eros, elementum pulvinar ante rutrum vel.</p>
    <p class="body">Proin varius iaculis orci, nec pretium purus porttitor et. Morbi arcu elit, porta et imperdiet ut, gravida et justo. Mauris sed mollis libero. Donec eleifend, enim at ullamcorper dictum, purus nisi imperdiet elit, eget convallis ante diam et lacus. Fusce et vulputate lorem, eget vehicula sapien. Aliquam tempor lacus quam, vitae sollicitudin mauris vulputate eget.</p>
    <div class="count"><div><b>03</b>DAYS</div><div><b>15</b>HOURS</div><div><b>27</b>MIN</div><div><b>03</b>SEC</div></div>
  </div>
  <div class="arrow" style="left:622px;top:218px">‹</div>
  <div class="arrow" style="left:1019px;top:218px">›</div>
  <div class="offer-card">
    <span class="badge" style="left:118px;right:auto;top:14px">-10%</span>
    <div class="prod-img" role="img" aria-label="Orange chainsaw bar case"></div>
    <div class="info card" style="width:190px;height:150px;border:0;padding:0">
      <h4>RIM CYLINDERS</h4><div class="stars">★★★★★</div>
      <p>Aliquam bibendum lacus a turpis eleifend, et molestie turpis gravida. Cras sit amet augue quis orci rtrum pretium vel id quam.....</p>
      <div class="price" style="left:0;bottom:0"><s>$55.00</s>$35.00</div>
      <a class="btn-cart" style="right:0;bottom:-4px">ADD TO CART ▢</a>
    </div>
  </div>
</section>

<section class="products">
  <div class="wrap">
    <div class="side-panel">
      <h2>NEW PRODUCTS</h2>
      <p>Lorem ipsum dolor sit amet, consectetur adipiscing elit. Explicabo quam</p>
      <a class="btn-white">Shop Now!</a>
      <div class="gloves" role="img" aria-label="Pair of blue nitrile gloves"></div>
    </div>
    <div class="block-head"><span>New Products</span><a>SHOP ALL</a></div>
    <div class="cards">
      <div class="card"><span class="badge">-10%</span><div class="prod-img" role="img" aria-label="Orange hi-vis work shirt"></div><h4>RIM CYLINDERS</h4><div class="stars">★★★★★</div><p>Aliquam bibendum lacus a turpis eleifend, et molestie turpis gravida. Cras sit amet augue quis orci rtrum pretium vel id quam.....</p><div class="price"><s>$55.00</s>$35.00</div><a class="btn-cart">ADD TO CART ▢</a></div>
      <div class="card"><span class="badge new">NEW</span><div class="prod-img" role="img" aria-label="Orange safety helmet with visor and ear muffs"></div><h4>RIM CYLINDERS</h4><div class="stars">★★★★★</div><p>Aliquam bibendum lacus a turpis eleifend, et molestie turpis gravida. Cras sit amet augue quis orci rtrum pretium vel id quam.....</p><div class="price"><s>$55.00</s>$35.00</div><a class="btn-cart">ADD TO CART ▢</a></div>
      <div class="card" style="border:0"><span class="badge">-10%</span><div class="prod-img" role="img" aria-label="Orange chainsaw bar case"></div><h4>RIM CYLINDERS</h4><div class="stars">★★★★★</div><p>Aliquam bibendum lacus a turpis eleifend, et molestie turpis gravida. Cras sit amet augue quis orci rtrum pretium vel id quam.....</p><div class="price"><s>$55.00</s>$35.00</div><a class="btn-cart">ADD TO CART ▢</a></div>
    </div>
    <div class="arrow" style="left:225px;top:165px">‹</div>
    <div class="arrow" style="left:858px;top:165px">›</div>
  </div>
</section>

<section class="best">
  <div class="k">BEST OFFER AVAILABLE</div>
  <h2>GET 25% OFF OR NEXT DAY FREE SHIPPING</h2>
  <a class="btn">SHOP NOW</a>
  <div class="best-card" style="left:136px">
    <div class="corner"></div><span class="corner-t">BEST</span>
    <h3>BEST PRODUCT</h3>
    <p>Lorem Ipsum Dolor Sit Amet, Consectetur Adipiscing Elit, Sed Do Eiusmod Tempor Incididunt.</p>
    <a class="go">SHOP NOW</a>
    <div class="prod-img" role="img" aria-label="Orange hi-vis work shirt"></div>
  </div>
  <div class="best-card" style="left:609px">
    <div class="corner"></div><span class="corner-t">BEST</span>
    <h3>BEST PRODUCT</h3>
    <p>Lorem Ipsum Dolor Sit Amet, Consectetur Adipiscing Elit, Sed Do Eiusmod Tempor Incididunt.</p>
    <a class="go">SHOP NOW</a>
    <div class="prod-img" style="height:150px;top:60px" role="img" aria-label="Orange safety helmet with visor and ear muffs"></div>
  </div>
</section>

<section class="news">
  <h2>NEWSLETTER</h2>
  <p>subscribe our newsletter &amp; get upto 60% Discount</p>
  <form><input value="Enter Your E-Mail"><button type="button">SUBSCRIBE NOW</button></form>
</section>

<footer class="footer">
  <div class="wrap">
    <div class="brand"><span class="brand-dot"></span><span class="brand-name">Bluefern</span></div>
    <p class="about">Proin varius iaculis orci, nec pretium purus porttitor et. Morbi arcu elit, porta et imperdiet ut, gravida et justo. Mauris sed mollis libero.</p>
    <div class="soc"><span></span><span></span><span></span><span></span></div>
    <div class="fcol" style="left:301px"><h4>Quick Links</h4>About<br>Terms &amp; Conditions<br>Privacy Policy<br>Shop<br>Contact</div>
    <div class="fcol" style="left:451px"><h4>Support</h4>Help<br>Contact Us<br>Feedback<br>Unsubscribe<br>Reservations</div>
    <div class="fcol" style="left:601px;width:290px"><h4>Contact Us</h4>Address: lorem ipsum USA Lorem ipsum is dolor amet lorem ipsum<br>E-mail: info@example.com
      <div class="cards-pay"><span></span><span></span><span></span><span></span></div>
    </div>
  </div>
</footer>

<footer class="copy">Copyright 2023 bluefernworks All Rights</footer>

</body>
</html>
```